Business Card Design

We are a church looking for marketing business card. Contact info Pastors name and a map on the back. Service times. Looking for something to grab attention. Not looking for personal card more of a generic card to pass out to new potential visitors.

Industry/Entity Type

Marketing

Contact Information for Business Card

Willow Crest Community Church
418 Harlan Ridge Pkwy suite 3-C Jonesboro GA 30236
(770)555-0148
Wcccfellow.org
Pastor Martin Holloway
Sunday 12:00 pm
Wednesday prayer call 9:30 pm 7125550163 conference #2846137

```html
<!DOCTYPE html>
<html lang="en">
<head>
<meta charset="utf-8">
<title>Willow Crest Community Church – Business Card</title>
<link rel="stylesheet" href="https://fonts.googleapis.com/css2?family=Arimo:wght@400;700&display=swap">
<style>
  :root {
    --card-bg: #ffffff;
    --header-tint: #eef3d3;
    --ink: #1a1a1a;
    --accent-blue: #3a6fd0;
    --panel-blue: #3366cc;
    --panel-red: #7c0016;
    --panel-green: #33e010;
    --icon-disc: #dcc7ea;
    --icon-ink: #5a2fb0;
    --link-ink: #c03ad0;
    --cross-wood: #a0522d;
    --cross-dark: #5a2a10;
    --portrait-a: #b0774f;
    --portrait-b: #e0407a;
  }
  * { margin: 0; padding: 0; box-sizing: border-box; }
  html, body { width: 1200px; height: 702px; overflow: hidden; background: var(--card-bg); }
  body { font-family: "Arimo", Arial, sans-serif; color: var(--ink); }
  .card { position: relative; width: 1200px; height: 702px; background: var(--card-bg); overflow: hidden; }
  .header-arc { position: absolute; left: 0; top: 0; width: 1200px; height: 300px; }
  .church-name {
    position: absolute; left: 58px; top: 72px; width: 520px;
    display: flex; align-items: center; gap: 18px;
    font-size: 34px; font-weight: 700; line-height: 1.15; color: var(--ink);
  }
  .church-name .mark { flex: none; width: 22px; height: 22px; background: var(--ink); border-radius: 50%; }
  .portrait {
    position: absolute; left: 652px; top: 55px; width: 166px; height: 166px; border-radius: 50%;
    background: radial-gradient(circle at 40% 45%, var(--portrait-a) 0 45%, var(--portrait-b) 100%);
  }
  .pastor { position: absolute; left: 850px; top: 82px; }
  .pastor-name { font-size: 25px; line-height: 30px; }
  .pastor-rule { width: 260px; height: 1px; background: var(--ink); margin: 13px 0 0 4px; }
  .pastor-role { font-size: 24px; margin: 16px 0 0 1px; }
  .cross { position: absolute; left: 272px; top: 302px; width: 84px; height: 124px; }
  .services { position: absolute; left: 378px; top: 308px; font-size: 33px; line-height: 60px; }
  .service { display: flex; white-space: nowrap; }
  .service-label { color: var(--accent-blue); }
  .row-worship .service-label { width: 186px; }
  .row-worship .service-day { width: 197px; }
  .row-prayer .service-label { width: 190px; }
  .row-prayer .service-day { width: 193px; }
  .contact { position: absolute; top: 509px; height: 134px; display: flex; align-items: center; color: #fff; }
  .contact-address { left: 60px; width: 460px; background: var(--panel-blue); }
  .contact-web { left: 537px; width: 296px; background: var(--panel-red); }
  .contact-phone { left: 852px; width: 291px; background: var(--panel-green); }
  .contact-icon { flex: none; width: 58px; height: 58px; margin: 0 14px 0 24px; }
  .contact-text { font-size: 24px; line-height: 33px; }
  .contact-address .contact-icon { margin: 0 14px 0 20px; }
  .contact-address .contact-text { font-size: 21.5px; line-height: 32px; }
</style>
</head>
<body>
<main class="card">
  <svg class="header-arc" viewBox="0 0 1200 300" aria-hidden="true">
    <path d="M0 0 H1200 V128 Q600 400 0 160 Z" fill="var(--header-tint)"/>
  </svg>

  <div class="church-name"><span class="mark"></span><span>Willow Crest Community Church</span></div>

  <div class="portrait" role="img" aria-label="Portrait photo of Pastor Martin Holloway"></div>
  <div class="pastor">
    <p class="pastor-name">Pastor Martin Holloway</p>
    <div class="pastor-rule"></div>
    <p class="pastor-role">manager</p>
  </div>

  <svg class="cross" viewBox="0 0 84 124" aria-hidden="true">
    <path d="M32 2 H52 V30 H82 V50 H52 V122 H32 V50 H2 V30 H32 Z" fill="var(--cross-wood)" stroke="var(--cross-dark)" stroke-width="3"/>
  </svg>

  <div class="services">
    <div class="service row-worship"><span class="service-label">Worship</span><span class="service-day">Sunday</span><span>12:00 pm</span></div>
    <div class="service row-prayer"><span class="service-label">prayer call</span><span class="service-day">Wednesday</span><span>9:30 pm</span></div>
  </div>

  <div class="contact contact-address">
    <svg class="contact-icon" viewBox="0 0 58 58" aria-hidden="true">
      <circle cx="29" cy="29" r="29" fill="var(--icon-disc)"/>
      <path d="M15 29 L29 17 L43 29 M19 27 V41 H39 V27" fill="none" stroke="var(--icon-ink)" stroke-width="4" stroke-linejoin="round"/>
    </svg>
    <p class="contact-text">418 Harlan Ridge Pkwy suite 3-C<br>Jonesboro GA 30236</p>
  </div>

  <div class="contact contact-web">
    <svg class="contact-icon" viewBox="0 0 58 58" aria-hidden="true">
      <circle cx="29" cy="29" r="29" fill="var(--icon-disc)"/>
      <g fill="none" stroke="var(--link-ink)" stroke-width="4.5">
        <rect x="14" y="14" width="18" height="12" rx="6" transform="rotate(45 23 20)"/>
        <rect x="26" y="32" width="18" height="12" rx="6" transform="rotate(45 35 38)"/>
      </g>
    </svg>
    <p class="contact-text">Wcccfellow.org</p>
  </div>

  <div class="contact contact-phone">
    <svg class="contact-icon" viewBox="0 0 58 58" aria-hidden="true">
      <circle cx="29" cy="29" r="29" fill="var(--icon-disc)"/>
      <rect x="19" y="13" width="20" height="32" rx="3" fill="none" stroke="var(--icon-ink)" stroke-width="4"/>
      <circle cx="29" cy="39" r="2" fill="var(--icon-ink)"/>
    </svg>
    <p class="contact-text">(770)555-0148</p>
  </div>
</main>
</body>
</html>
```